Nutracuetical supplement label

Will be private labeling a variety of nutraceutical supplements for a holistic health and weight loss clinics. We have a trademarked logo and colors of green and blue. The green is: Pantone 376 c56 y100. The blue is: Pantone 301 C: 100% M: 40% Y: 0% K: 40%.
The look should be fresh with a smacking of clinical rather than earthy. Lots of white space without looking bland. Please use both our colors and refer to our website for other ideas VelmoraCare.com.
Updates
Project Deadline Extended
Reason: Lots of good designs. I will be asking each of the (3) finalists for a minor change and make a final decision on Oct 20th. Thank you for your designs and creativity.
Target Market(s)
Weight loss patients investing in clinically proven program.
Industry/Entity Type
Health
Look and feel
Each slider illustrates characteristics of the customer's brand and the style your logo design should communicate.

```html
<!DOCTYPE html>
<html lang="en">
<head>
<meta charset="utf-8">
<title>Velmora Care – Supplement Labels</title>
<link href="https://fonts.googleapis.com/css2?family=Questrial&display=swap" rel="stylesheet">
<style>
  :root {
    --brand-blue: #1a63ad;
    --brand-green: #6abf3c;
    --label-white: #ffffff;
    --page-bg: #f1f2f3;
    --name-grey: #8c8c8c;
    --fruit-yellow: #f7c65a;
    --fruit-orange: #ee8a2c;
    --fruit-red: #c0392b;
    --fruit-green: #9cc24a;
    --fruit-brown: #8a5a3a;
    --portrait-light: #f8f6f1;
    --portrait-leaf: #dfe9d6;
    --portrait-skin: #e8c3a8;
    --portrait-hair: #9a6a4a;
    --portrait-pink: #e6a6c0;
  }
  * { box-sizing: border-box; margin: 0; padding: 0; }
  html, body {
    width: 1196px;
    height: 1200px;
    overflow: hidden;
  }
  body {
    background: var(--page-bg);
    font-family: "Questrial", sans-serif;
    position: relative;
  }
  .label {
    position: absolute;
    top: 200px;
    width: 510px;
    height: 800px;
    background: var(--label-white);
    box-shadow: 0 2px 10px rgba(0,0,0,0.08);
  }
  .label--fruit { left: 48px; }
  .label--wellness { left: 638px; }

  .brand-block {
    position: absolute;
    top: 60px;
    left: 50%;
    transform: translateX(-50%);
    width: 340px;
    height: 168px;
    background: var(--brand-blue);
    color: var(--label-white);
    text-align: center;
    padding-top: 50px;
  }
  .brand-name {
    display: flex;
    align-items: center;
    justify-content: center;
    gap: 10px;
    font-size: 30px;
    letter-spacing: 2px;
    line-height: 1;
    white-space: nowrap;
  }
  .brand-mark {
    flex-shrink: 0;
    width: 18px;
    height: 18px;
    border-radius: 50%;
    background: var(--brand-green);
  }
  .brand-tagline {
    margin-top: 30px;
    font-size: 15px;
    white-space: nowrap;
  }

  .product-name {
    position: absolute;
    top: 256px;
    width: 100%;
    text-align: center;
    color: var(--name-grey);
    font-size: 36px;
    font-weight: 400;
    letter-spacing: 1px;
    white-space: nowrap;
  }

  .photo-ring {
    position: absolute;
    top: 330px;
    left: 50%;
    transform: translateX(-50%);
    width: 370px;
    height: 370px;
    border-radius: 50%;
    border: 14px solid var(--brand-green);
    overflow: hidden;
  }
  .photo-ring svg { display: block; width: 100%; height: 100%; }

  .dosage {
    position: absolute;
    left: 28px;
    bottom: 48px;
    color: var(--brand-blue);
    font-size: 28px;
  }
</style>
</head>
<body>

  <section class="label label--fruit">
    <div class="brand-block">
      <div class="brand-name"><span class="brand-mark"></span>VELMORA CARE</div>
      <div class="brand-tagline">Maximize Your Weight Health Journey</div>
    </div>
    <h2 class="product-name">PRODUCT NAME</h2>
    <div class="photo-ring">
      <svg role="img" aria-label="Photo of assorted fresh fruit: oranges, peaches, coconut, pomegranate and lemons" viewBox="0 0 100 100" preserveAspectRatio="none">
        <defs>
          <linearGradient id="fruitTones" x1="0" y1="0" x2="1" y2="1">
            <stop offset="0%" stop-color="var(--fruit-green)"/>
            <stop offset="22%" stop-color="var(--fruit-orange)"/>
            <stop offset="45%" stop-color="var(--fruit-brown)"/>
            <stop offset="62%" stop-color="var(--fruit-red)"/>
            <stop offset="80%" stop-color="var(--fruit-yellow)"/>
            <stop offset="100%" stop-color="var(--fruit-orange)"/>
          </linearGradient>
        </defs>
        <rect width="100" height="100" fill="url(#fruitTones)"/>
      </svg>
    </div>
    <div class="dosage">220mg</div>
  </section>

  <section class="label label--wellness">
    <div class="brand-block">
      <div class="brand-name"><span class="brand-mark"></span>VELMORA CARE</div>
      <div class="brand-tagline">Maximize Your Weight Health Journey</div>
    </div>
    <h2 class="product-name">PRODUCT NAME</h2>
    <div class="photo-ring">
      <svg role="img" aria-label="Portrait photo of a woman holding a pink lotus flower against a soft light background" viewBox="0 0 100 100" preserveAspectRatio="none">
        <defs>
          <linearGradient id="portraitTones" x1="0" y1="0.2" x2="1" y2="0.8">
            <stop offset="0%" stop-color="var(--portrait-light)"/>
            <stop offset="30%" stop-color="var(--portrait-leaf)"/>
            <stop offset="50%" stop-color="var(--portrait-light)"/>
            <stop offset="72%" stop-color="var(--portrait-skin)"/>
            <stop offset="100%" stop-color="var(--portrait-hair)"/>
          </linearGradient>
          <linearGradient id="lotusTone" x1="0" y1="0" x2="0" y2="1">
            <stop offset="0%" stop-color="var(--portrait-pink)" stop-opacity="0"/>
            <stop offset="100%" stop-color="var(--portrait-pink)" stop-opacity="0.45"/>
          </linearGradient>
        </defs>
        <rect width="100" height="100" fill="url(#portraitTones)"/>
        <rect width="100" height="100" fill="url(#lotusTone)"/>
      </svg>
    </div>
    <div class="dosage">220mg</div>
  </section>

</body>
</html>
```